Business Card Design Project

A business card for a new company in Ontario Canada called Build for Growth. It is a consulting company which uses Brixo as the medium for facilitation.

The target market is for senior leaders in healthcare and social services.

Industry/Entity Type

Healthcare

Requirements
Must have
• The name Build For Growth
Dana Montreuil RRT, B Ed (AD ed).
Tacticraft Facililitator (R)

Tag Line
Engaging Transforming and Innovative
The attached logo

danamontreuil@examplemail.com
416-555-0147
Should not have
• Lime green
Times New Roman or Arial font
Do not include Brixo bricks on the card.

```html
<!DOCTYPE html>
<html lang="en">
<head>
<meta charset="utf-8">
<title>Build For Growth – Business Card</title>
<link rel="stylesheet" href="https://fonts.googleapis.com/css2?family=Maven+Pro:wght@400;500;700&family=Cabin+Sketch:wght@400;700&display=swap">
<style>
  :root {
    --bg-top: #ffffff;
    --bg-bottom: #dcdcdc;
    --card: #ffffff;
    --teal: #1f8a70;
    --purple: #6b2c8f;
    --blue: #3aa6dc;
    --ink: #2e2e2e;
    --muted: #7a7a7a;
  }
  * { box-sizing: border-box; margin: 0; padding: 0; }
  html, body {
    width: 1200px; height: 456px; overflow: hidden;
  }
  body {
    position: relative;
    background: linear-gradient(180deg, var(--bg-top) 0%, #f2f2f2 45%, var(--bg-bottom) 100%);
    font-family: "Maven Pro", sans-serif;
  }
  .card {
    position: absolute;
    top: 83px;
    width: 513px;
    height: 287px;
    background: var(--card);
    border-radius: 22px;
    overflow: hidden;
    box-shadow: 0 2px 6px rgba(0,0,0,0.18), 0 0 0 1px rgba(0,0,0,0.05);
  }
  .card--front { left: 73px; }
  .card--back { left: 615px; }

  .brand {
    position: absolute;
    top: 71px;
    display: flex;
    flex-direction: column;
    align-items: center;
  }
  .brand__dot {
    width: 90px; height: 90px;
    border-radius: 50%;
    background: var(--purple);
  }
  .brand__name {
    font-family: "Maven Pro", sans-serif;
    font-weight: 500;
    font-size: 14px;
    letter-spacing: 1.5px;
    text-transform: uppercase;
    color: var(--ink);
    white-space: nowrap;
  }
  .card--front .brand { left: 0; right: 0; }
  .card--front .brand__name { margin-top: 52px; }
  .card--back .brand { left: 40px; width: 150px; }
  .card--back .brand__name { margin-top: 42px; }

  .divider {
    position: absolute;
    left: 227px; top: 46px;
    width: 2px; height: 170px;
    background: linear-gradient(180deg, var(--teal), var(--blue));
  }
  .contact {
    position: absolute;
    left: 273px; top: 72px;
  }
  .contact__name {
    font-size: 22px;
    font-weight: 500;
    color: var(--blue);
    margin-bottom: 4px;
  }
  .contact__title {
    font-size: 14px;
    line-height: 20px;
    color: var(--muted);
  }
  .contact__email {
    margin-top: 20px;
    font-size: 14px;
    color: var(--teal);
  }
  .contact__phone {
    font-size: 14px;
    font-weight: 700;
    color: var(--teal);
    line-height: 20px;
  }

  .tagline {
    position: absolute;
    left: 0; right: 0; bottom: 0;
    height: 39px;
    display: flex;
    font-family: "Cabin Sketch", sans-serif;
    font-size: 19px;
    text-transform: uppercase;
    color: #ffffff;
    letter-spacing: 0.5px;
  }
  .tagline__part {
    display: flex;
    align-items: center;
    justify-content: center;
    white-space: nowrap;
  }
  .tagline__part--teal { width: 144px; background: var(--teal); }
  .tagline__part--purple { width: 161px; background: var(--purple); }
  .tagline__part--blue { flex: 1; background: var(--blue); }
</style>
</head>
<body>
  <section class="card card--front" aria-label="Card front">
    <div class="brand">
      <span class="brand__dot"></span>
      <span class="brand__name">Build For Growth</span>
    </div>
  </section>

  <section class="card card--back" aria-label="Card back">
    <div class="brand">
      <span class="brand__dot"></span>
      <span class="brand__name">Build For Growth</span>
    </div>
    <span class="divider"></span>
    <div class="contact">
      <p class="contact__name">Dana Montreuil</p>
      <p class="contact__title">RRT, B Ed (AD ed).</p>
      <p class="contact__title">Tacticraft Facililitator (R)</p>
      <p class="contact__email">danamontreuil@examplemail.com</p>
      <p class="contact__phone">416-555-0147</p>
    </div>
    <div class="tagline">
      <span class="tagline__part tagline__part--teal">Engaging</span>
      <span class="tagline__part tagline__part--purple">Transforming</span>
      <span class="tagline__part tagline__part--blue">and Innovative</span>
    </div>
  </section>
</body>
</html>
```